A simple Chatterbook Ad (not Chatterbook Page) for weight loss surgery

It’s a simple ad in terms of the text.

The text should say:
Curious about weight loss surgery?
This 30 second quiz will tell you which procedure will suit you best

I'm open to variations in the text if it is thought to enhance the ad.

Targeted towards obese individuals who have been unable to lose weight with diet and exercise. My industry is weight loss surgery – webpage www.marcusbellweather.com.au. Clicking the ad leads to a quiz on my webpage relating to weight loss surgery. Most frequent users of this service are females (75%) between ages of 35 and 55 years.

Successful weight loss surgery can enable individuals who have been unable to lose weight to lose a substantial amount of the excess weight they are carrying to be healthier and happier.

```html
<!DOCTYPE html>
<html lang="en">
<head>
<meta charset="utf-8">
<title>Weight Loss Surgery Quiz Ad</title>
<link rel="stylesheet" href="https://fonts.googleapis.com/css2?family=Montserrat:wght@400;500;900&display=swap">
<style>
  :root {
    --page: #ffffff;
    --navy: #0d3a66;
    --royal: #0b63d8;
    --sky: #0aa8f5;
    --white: #ffffff;
    --brand: #1f7f7a;
    --grey: #5a6470;
  }
  * { margin: 0; padding: 0; box-sizing: border-box; }
  html, body {
    width: 1055px; height: 1200px; overflow: hidden;
    background: var(--page);
    font-family: "Montserrat", sans-serif;
  }
  .ad {
    position: absolute; left: 92px; top: 165px;
    width: 871px; height: 871px; overflow: hidden;
    box-shadow: 0 20px 50px rgba(0,0,0,0.18);
  }
  .ad-art { position: absolute; inset: 0; }
  .brand {
    position: absolute; left: 180px; top: 198px; width: 300px;
    text-align: center; color: var(--brand);
  }
  .brand-mark {
    display: block; width: 56px; height: 56px; margin: 0 auto 16px;
    border-radius: 50%; background: var(--brand);
  }
  .brand-name {
    font-weight: 500; font-size: 24px; letter-spacing: 0.5px; line-height: 1;
  }
  .brand-role {
    margin-top: 4px; font-size: 9.5px; letter-spacing: 1.6px;
    text-transform: uppercase; color: var(--grey);
  }
  .headline {
    position: absolute; left: 154px; top: 344px;
    line-height: 1; white-space: nowrap;
  }
  .headline-lead {
    display: block; font-weight: 400; font-size: 70px; color: var(--navy);
    letter-spacing: -0.5px;
  }
  .headline-strong {
    display: block; font-weight: 900; font-size: 64px; color: var(--royal);
    margin-top: 0; letter-spacing: -0.5px;
  }
  .headline-accent { color: var(--sky); }
  .subline {
    position: absolute; left: 232px; top: 571px; width: 370px;
    text-align: center; font-weight: 500; font-size: 22px; line-height: 33px;
    color: var(--navy);
  }
</style>
</head>
<body>
  <section class="ad" aria-label="Weight loss surgery quiz advert">
    <svg class="ad-art" width="871" height="871" viewBox="0 0 871 871">
      <defs>
        <linearGradient id="bg-tone" x1="0" y1="0" x2="1" y2="1">
          <stop offset="0" stop-color="#0d3f8f"/>
          <stop offset="0.5" stop-color="#1456b4"/>
          <stop offset="1" stop-color="#0b3a84"/>
        </linearGradient>
        <linearGradient id="mark-fill" gradientUnits="userSpaceOnUse" x1="0" y1="140" x2="0" y2="960">
          <stop offset="0" stop-color="#04aaff"/>
          <stop offset="0.55" stop-color="#0a8eef"/>
          <stop offset="1" stop-color="#0a5fd6"/>
        </linearGradient>
      </defs>
      <rect class="backdrop" width="871" height="871" fill="url(#bg-tone)" role="img" aria-label="Blue network of medical icons: hearts, crosses, syringe, caduceus and pills"/>
      <path class="ring" d="M612 99 A381 381 0 1 0 612 771" fill="none" stroke="var(--white)" stroke-width="5.5" stroke-linecap="round"/>
      <circle cx="612" cy="99" r="6" fill="var(--white)"/>
      <circle cx="612" cy="771" r="6" fill="var(--white)"/>
      <circle class="spotlight" cx="435" cy="436" r="319" fill="var(--white)"/>

      <g class="question-mark" transform="scale(0.8065)" stroke="var(--white)" stroke-width="16" stroke-linejoin="round">
        <path class="question-hook" fill="url(#mark-fill)"
          d="M614 401
             C614 240 740 140 880 140
             C1050 140 1150 240 1150 380
             C1150 500 1070 560 1020 620
             C985 662 976 690 976 721
             L766 721
             C766 640 800 585 858 525
             C905 478 931 450 931 396
             C931 356 905 336 866 336
             C826 336 795 360 790 401
             Z"/>
        <ellipse class="question-dot" cx="871" cy="851" rx="118" ry="110" fill="url(#mark-fill)"/>
        <ellipse class="dot-highlight" cx="871" cy="851" rx="60" ry="50" fill="none" stroke-width="9"/>
      </g>
    </svg>

    <div class="brand">
      <span class="brand-mark"></span>
      <p class="brand-name">Marcus Bellweather</p>
      <p class="brand-role">General, Upper GI &amp; Bariatric Surgeon</p>
    </div>

    <h1 class="headline">
      <span class="headline-lead">Curious about</span>
      <span class="headline-strong">WEIGHT LOSS</span>
      <span class="headline-strong headline-accent">SURGERY?</span>
    </h1>

    <p class="subline">This 30 second quiz will tell you which procedure will suit you best</p>
  </section>
</body>
</html>
```